Building Company Business Card Design

Need a design for a business card:
It needs to have: Name, Phone, Facebook link, Website, email
i would also like a list of works we undertake:
-New Homes
-Extensions, Renovations & Bathrooms
-Decking, Carports, Sheds (Residential and Industrial)
-Carpentry
-Fences, Patios & Pergolas

Name, Phone, Facebook link, Website, email + details of services provided listed in description

```html
<!DOCTYPE html>
<html lang="en">
<head>
<meta charset="utf-8">
<title>Northgate Homes – Business Cards</title>
<link href="https://fonts.googleapis.com/css2?family=Montserrat:wght@400;500;700;800&display=swap" rel="stylesheet">
<style>
  :root {
    --bg: #d9d8d5;
    --card: #1a1a1b;
    --green: #38b54f;
    --grey: #8a8a8a;
    --dark-grey: #5a5a5a;
    --white: #ffffff;
  }
  * { margin: 0; padding: 0; box-sizing: border-box; }
  html, body { width: 1200px; height: 801px; overflow: hidden; }
  body {
    background: var(--bg);
    font-family: "Montserrat", sans-serif;
    position: relative;
  }
  .card {
    position: absolute;
    top: 236px;
    width: 540px;
    height: 318px;
    background: var(--card);
    border-bottom: 6px solid var(--green);
    overflow: hidden;
    box-shadow: 0 6px 18px rgba(0,0,0,0.25);
  }
  .card--contact { left: 40px; }
  .card--services { left: 620px; }

  /* contact side */
  .contact-panel {
    position: absolute;
    right: 0; top: 0;
    width: 210px; height: 100%;
  }
  .company-name {
    position: absolute;
    left: 34px; top: 40px;
    color: var(--white);
    font-weight: 700;
    font-size: 22px;
    line-height: 1.1;
    letter-spacing: 0.5px;
  }
  .company-name small {
    display: block;
    font-size: 11px;
    letter-spacing: 1px;
    margin-top: 3px;
  }
  .person {
    position: absolute;
    left: 34px; top: 118px;
  }
  .person-marker {
    position: absolute;
    left: 0; top: 128px;
    width: 18px; height: 28px;
    background: var(--green);
  }
  .person-name {
    color: var(--green);
    font-weight: 700;
    font-size: 20px;
    letter-spacing: 1px;
  }
  .person-role {
    color: var(--white);
    font-size: 12px;
    margin-top: 2px;
  }
  .contact-list {
    position: absolute;
    left: 34px; top: 188px;
    list-style: none;
  }
  .contact-list li {
    display: flex;
    align-items: center;
    gap: 8px;
    color: var(--white);
    font-size: 12.5px;
    line-height: 24px;
  }
  .contact-list svg { width: 12px; height: 12px; fill: var(--green); flex: none; }

  /* services side */
  .brand {
    position: absolute;
    left: 0; right: 0; top: 80px;
    text-align: center;
    color: var(--white);
    font-weight: 700;
    font-size: 34px;
    line-height: 1.05;
    letter-spacing: 1px;
  }
  .brand small {
    display: block;
    font-size: 16px;
    letter-spacing: 2px;
    margin-top: 4px;
  }
  .services-heading {
    position: absolute;
    left: 40px; right: 40px; top: 196px;
    display: flex;
    align-items: center;
    gap: 10px;
    color: var(--green);
    font-weight: 800;
    font-size: 13px;
    letter-spacing: 1px;
  }
  .services-heading::before,
  .services-heading::after {
    content: "";
    flex: 1;
    height: 1px;
    background: var(--green);
  }
  .services-list {
    position: absolute;
    left: 20px; right: 20px; top: 226px;
    text-align: center;
    color: var(--white);
    font-size: 12.5px;
    line-height: 24px;
  }
  .services-list .dot { color: var(--green); font-weight: 800; margin: 0 4px; }
</style>
</head>
<body>

<section class="card card--contact" aria-label="Business card, contact side">
  <svg class="contact-panel" viewBox="0 0 210 312" preserveAspectRatio="none" aria-hidden="true">
    <polygon points="40,0 210,0 210,312 110,312" fill="#2a2a2b"/>
    <polygon points="60,0 210,0 210,70 80,70" fill="var(--green)"/>
  </svg>
  <h1 class="company-name">NORTHGATE HOMES<small>AND DEVELOPMENTS PTY LTD</small></h1>
  <span class="person-marker"></span>
  <div class="person">
    <p class="person-name">DANIEL HARPER</p>
    <p class="person-role">Managing Director</p>
  </div>
  <ul class="contact-list">
    <li><svg viewBox="0 0 24 24"><path d="M6.6 10.8a15.2 15.2 0 0 0 6.6 6.6l2.2-2.2a1 1 0 0 1 1-.25 11.4 11.4 0 0 0 3.6.57 1 1 0 0 1 1 1V20a1 1 0 0 1-1 1A17 17 0 0 1 3 4a1 1 0 0 1 1-1h3.5a1 1 0 0 1 1 1c0 1.25.2 2.45.57 3.6a1 1 0 0 1-.25 1z"/></svg>555-210-4471</li>
    <li><svg viewBox="0 0 24 24"><path d="M2 5h20v14H2zm2 2v.5l8 5 8-5V7z"/></svg>info@northgatehomespty.com</li>
    <li><svg viewBox="0 0 24 24"><circle cx="12" cy="12" r="10"/></svg>www.northgatehomespty.com</li>
    <li><svg viewBox="0 0 24 24"><circle cx="12" cy="12" r="10"/></svg>@northgatehomespty</li>
  </ul>
</section>

<section class="card card--services" aria-label="Business card, services side">
  <h2 class="brand">NORTHGATE HOMES<small>AND DEVELOPMENTS PTY LTD</small></h2>
  <h3 class="services-heading">OUR SERVICES</h3>
  <p class="services-list">
    New Homes<span class="dot">•</span>Extensions, Renovations &amp; Bathrooms<span class="dot">•</span>Carpentry<br>
    Decking, Carports, Sheds<span class="dot">•</span>Fences, Patios &amp; Pergolas
  </p>
</section>

</body>
</html>
```